High-end dermatology office brochure design

Corvellan Skin and Laser is a high-end dermatology practice that specializes in custom skin care solutions, and skin cancer surveillance and treatment. Brochure should be elegant, but informative to attract high-end customers.

Target Market(s)

Men and women 27-60

Industry/Entity Type

Office

Requirements
Must have
• Attached document has required copy, including, websites, address and company phone number
Nice to have
• images

```html
<!DOCTYPE html>
<html lang="en">
<head>
<meta charset="utf-8">
<title>Corvellan Skin and Laser – Brochure</title>
<link rel="stylesheet" href="https://fonts.googleapis.com/css2?family=Roboto+Condensed:wght@300;400&family=Gelasio:ital@1&display=swap">
<style>
  :root {
    --purple: #6b3b8c;
    --purple-soft: #8a5aa8;
    --green: #bccf5a;
    --green-pale: #dde8b0;
    --ink: #4d4d4d;
    --ink-soft: #666;
    --paper: #ffffff;
    --backdrop: #e6e6e6;
  }
  * { margin: 0; padding: 0; box-sizing: border-box; }
  html, body { width: 1200px; height: 886px; overflow: hidden; }
  body {
    background: var(--backdrop);
    font-family: "Roboto Condensed", "Arial Narrow", sans-serif;
    color: var(--ink);
    position: relative;
  }
  .spread {
    position: absolute; left: 62px; top: 48px;
    width: 1080px; height: 772px;
    background: var(--paper);
    box-shadow: 0 4px 18px rgba(0,0,0,.25);
    overflow: hidden;
  }
  .spread-art { position: absolute; inset: 0; }
  .page-fold {
    position: absolute; left: 540px; top: 0; width: 40px; height: 772px;
    background: linear-gradient(90deg, rgba(0,0,0,.08), rgba(0,0,0,0));
  }
  .abs { position: absolute; }

  /* Left page */
  .wordmark {
    color: var(--purple); font-weight: 400; line-height: 1.05;
    text-align: center;
  }
  .wordmark-left { left: 140px; top: 312px; width: 260px; font-size: 30px; }
  .wordmark-right { left: 730px; top: 652px; width: 300px; font-size: 32px; }
  .wordmark small { display: block; font-size: .7em; }

  .contact { left: 120px; top: 390px; width: 300px; text-align: center; }
  .contact .phone { font-size: 25px; color: var(--ink); letter-spacing: .5px; }
  .contact .web { font-size: 14px; letter-spacing: 1px; color: var(--ink); line-height: 18px; margin-top: 6px; }

  .location { position: absolute; top: 490px; width: 140px; text-align: center; }
  .location h3 { font-weight: 400; font-size: 9.5px; color: var(--ink); margin-bottom: 14px; }
  .map-ring {
    width: 118px; height: 118px; margin: 0 auto; border-radius: 50%;
    border: 4px solid var(--green);
    background: linear-gradient(135deg, #eceae4, #d9d6cc);
  }
  .location address {
    font-style: normal; font-size: 7.5px; line-height: 9px; color: #333; margin-top: 6px;
  }
  .loc-one { left: 48px; }
  .loc-two { left: 198px; }
  .loc-three { left: 346px; }

  .insurance-pill {
    left: 65px; top: 704px; width: 384px; height: 24px; border-radius: 12px;
    background: var(--green); color: #4b5a1c;
    font-size: 12.5px; text-align: center; line-height: 24px;
  }

  /* Right page */
  .tagline { left: 579px; top: 29px; font-size: 25px; font-weight: 300; color: var(--ink-soft); white-space: nowrap; }
  .headline { left: 579px; top: 62px; font-size: 39.5px; font-weight: 400; color: var(--ink); letter-spacing: .3px; white-space: nowrap; }
  .care-pill {
    left: 579px; top: 122px; width: 376px; height: 58px; border-radius: 29px;
    background: linear-gradient(180deg, #c9d96e, var(--green));
    box-shadow: 0 6px 8px -6px rgba(0,0,0,.35);
    font-family: "Gelasio", Georgia, serif; font-style: italic;
    font-size: 36px; color: var(--purple); text-align: center; line-height: 56px;
    letter-spacing: 1px;
  }
  .intro { left: 579px; top: 204px; width: 400px; font-size: 13px; line-height: 16px; color: var(--ink); white-space: nowrap; }
  .intro p + p { margin-top: 6px; }

  .spa-ring {
    left: 578px; top: 360px; width: 216px; height: 216px; border-radius: 50%;
    background: var(--green-pale); padding: 12px;
  }
  .spa-photo {
    width: 100%; height: 100%; border-radius: 50%;
    background: radial-gradient(circle at 40% 40%, #e6c7a4, #a07c54 55%, #5e6e3a);
  }
  .logo-band {
    left: 718px; top: 640px; width: 362px; height: 108px;
    background: rgba(255,255,255,.55);
  }
</style>
</head>
<body>
  <main class="spread">
    <svg class="spread-art" viewBox="0 0 1080 772" width="1080" height="772">
      <defs>
        <linearGradient id="flowerTone" x1="0" y1="0" x2="1" y2="1">
          <stop offset="0" stop-color="#8a5aa8"/>
          <stop offset="1" stop-color="#6b3b8c"/>
        </linearGradient>
        <linearGradient id="skinTone" x1="0" y1="0" x2="1" y2="0">
          <stop offset="0" stop-color="#f3e4da"/>
          <stop offset="1" stop-color="#e7c7b3"/>
        </linearGradient>
      </defs>
      <path class="curve-green" d="M0,0 H510 C400,70 330,210 220,280 C130,335 50,360 0,400 Z" fill="#bccf5a"/>
      <path class="flower-photo" role="img" aria-label="Purple-tinted flower photograph"
            d="M0,0 H490 C380,60 300,200 200,260 C120,310 40,330 0,370 Z" fill="url(#flowerTone)"/>
      <path class="curve-green" d="M910,0 H1080 V270 C1050,160 1000,60 910,0 Z" fill="#bccf5a"/>
      <path class="curve-purple" d="M955,0 H1080 V200 C1060,110 1020,40 955,0 Z" fill="#6b3b8c"/>
      <path class="portrait-photo" role="img" aria-label="Close-up portrait photograph of a woman with clear skin"
            d="M730,420 L1080,190 V747 H770 C745,640 725,520 730,420 Z" fill="url(#skinTone)"/>
      <path class="curve-purple" d="M540,772 V690 C610,560 720,440 1080,180 V198 C770,420 680,560 640,772 Z" fill="#6b3b8c"/>
      <path class="curve-green" d="M648,772 C670,600 730,500 820,420 L832,428 C745,505 695,610 690,772 Z" fill="#bccf5a"/>
    </svg>
    <div class="page-fold"></div>

    <!-- Left page -->
    <div class="abs wordmark wordmark-left">Corvellan<small>Skin and Laser</small></div>
    <div class="abs contact">
      <div class="phone">480-555-0142</div>
      <div class="web">corvellanskincare.com<br>Shop at glowpantryboutique.com</div>
    </div>

    <section class="location loc-one">
      <h3>Sunridge, Arizona</h3>
      <div class="map-ring" role="img" aria-label="Street map of the Sunridge office"></div>
      <address>Corvellan Skin &amp; Laser<br>2710 E Sagebrush Rd<br>Building #4<br>Suite #120<br>Sunridge, AZ 85990</address>
    </section>
    <section class="location loc-two">
      <h3>Mesa Alta, Arizona</h3>
      <div class="map-ring" role="img" aria-label="Street map of the Mesa Alta office"></div>
      <address>Desert Bloom Skin Studio<br>Located in Wellpoint Center<br>8640 E Canyon View<br>Suite #210<br>Mesa Alta, AZ 85997</address>
    </section>
    <section class="location loc-three">
      <h3>Lanakoa, Hawaii</h3>
      <div class="map-ring" role="img" aria-label="Street map of the Lanakoa office"></div>
      <address>Island Skin Cancer Center<br>Harborview Plaza<br>Suite #305<br>720 Kapena Blvd.<br>Lanakoa, HI 96899</address>
    </section>

    <div class="abs insurance-pill">We accept most major insurances and offer affordable self-pay rates.</div>

    <!-- Right page -->
    <div class="abs tagline">A personalized approach to skin care</div>
    <h1 class="abs headline">RESULTS YOU CAN SEE</h1>
    <div class="abs care-pill">Care you can feel</div>
    <div class="abs intro">
      <p>Let us create a custom skin care regimen that best fits your medical and<br>personal needs.</p>
      <p>We pride ourselves on providing premium skin care, to patients of all<br>ages, with an honest and attentive approach. We’re also proud to be<br>leaders in skin cancer surveillance and specialize in the diagnosis<br>and treatment of skin cancer.</p>
    </div>
    <div class="abs spa-ring">
      <div class="spa-photo" role="img" aria-label="Photograph of a relaxing facial massage"></div>
    </div>
    <div class="abs logo-band"></div>
    <div class="abs wordmark wordmark-right">Corvellan<small>Skin and Laser</small></div>
  </main>
</body>
</html>
```